Therapist Business Card Design

We need a business card design for our therapists. We are an all natural day spa. We focus on helping people look good, feel great in a safe environment. Majority of your clientele are between 32-45. They are sophisticated working women. We like a business card design that looks neutral to attract men and women. We position ourselves as the experts in spa and wellness. We like a card that look fun, modern and classy (that's a tough one..lol). These card will serve a purpose of marketing us to our client and their friends. The final design should communicate organic, safe and contemporary. Our current logo is green, white and brown (we would like to switch our current logo green to pale meadow from Dalworth Penning). Our spa paint will also be pale meadow, off white and coffee brown. Please check us out on www.qovalespa.example

Target Market(s)

Higher end clientele. Between 30-50 years old, male and female. Health conscious.
Also like to stay fashionable

Industry/Entity Type

Beauty Salon

Contact Information for Business Card

Front: Logo, slogan, therapist name and contact information, business contact info, Welcome offer
$119/ Facial, Massage, Mani & Pedi combo
Open Tue- Sun
Gift Cards Available
Walk-Ins Welcome
Back: spa logo, social media logos, The best compliment is a referral. Receive 1,000 CALMPerks points for each you and your friend when you referral a new friend to us**.
You
Phone
Email
Your friend
Phone
Email
Spot light--- GET 1,000 points
Google map image
business info
Small print:
*Welcome package offer valid for first-time Guests only. Includes a Renewal mani& pedi combo, 30 min relaxation massage, and a Renewal facial. Prices subject to change.
**CALMPerks points may only be given when a new guest purchase a minimum of $35 from us. Cannot be combined with other specials.

Font styles to use
Sans Serif

Requirements
Must have
• A clean and natural look and feel. Since we are a higher end spa, we would like for our business card to speaks that expensive look and quality. Our color scheme are coffee brown, green (pale meadow), white.
• Spot light of selling points:
• Front: Slogan, Welcome offer
• Back: Get 1,000 points
Nice to have
• Image of an illusion of white linen, or minty cloud, relax and calming.
Should not have
• Clutter

```html
<!DOCTYPE html>
<html lang="en">
<head>
<meta charset="utf-8">
<title>Qovale Day Spa – Therapist Card</title>
<link rel="stylesheet" href="https://fonts.googleapis.com/css2?family=Roboto+Condensed:wght@300;400;700&display=swap">
<style>
  :root{
    --meadow:#9db58a;
    --coffee:#4a3426;
    --ink:#2f2a26;
    --offwhite:#f1f0ea;
    --paper:#ffffff;
    --stage:#e3e4e2;
    --rule:#8a8a84;
    --map-a:#e9e6df;
  }
  *{box-sizing:border-box;margin:0;padding:0}
  html,body{width:1200px;height:864px;overflow:hidden}
  body{background:var(--stage);font-family:"Roboto Condensed",Arial,sans-serif;color:var(--ink);position:relative}
  .panel{position:absolute;width:540px;height:360px;background:var(--offwhite);box-shadow:0 2px 8px rgba(0,0,0,.12);overflow:hidden}
  .cover{left:40px;top:50px;background:var(--paper)}
  .offer{left:40px;top:454px}
  .referral{left:620px;top:50px}
  .contact{left:620px;top:454px}

  .brand{display:flex;align-items:center;gap:16px}
  .brand-dot{border-radius:50%;background:var(--meadow);flex:none}
  .brand-name{color:var(--coffee);font-weight:400;line-height:1;white-space:nowrap}

  .cover .brand{position:absolute;left:60px;top:70px}
  .cover .brand-dot{width:96px;height:96px}
  .cover .brand-name{font-size:46px}
  .slogan{position:absolute;left:176px;top:170px;font-size:34px;font-weight:300;color:var(--meadow)}
  .url-band{position:absolute;left:0;right:0;top:232px;height:58px;background:var(--meadow);display:flex;align-items:center;justify-content:center;font-size:30px;color:var(--coffee)}
  .social{position:absolute;left:0;right:0;top:306px;display:flex;justify-content:center;gap:8px}
  .social span{width:24px;height:24px;background:var(--meadow)}

  .offer-box{margin:22px 22px 0;background:var(--paper);border-radius:12px;padding:12px 16px;text-align:center}
  .offer-title{font-size:18px;font-weight:700;text-decoration:underline;color:var(--coffee)}
  .offer-line{font-size:20px;margin-top:4px}
  .feature{text-align:center;font-size:20px;font-weight:700;color:var(--coffee);margin-top:14px}
  .hours{margin:14px 22px 0;background:var(--paper);border-radius:12px;padding:10px 16px}
  .hours-title{text-align:center;font-size:18px;font-weight:700;color:var(--coffee)}
  .hours-grid{display:grid;grid-template-columns:1fr 1fr;font-size:18px;margin-top:4px}
  .therapist{margin:12px 22px 0}
  .therapist-name{font-size:26px;color:var(--coffee)}
  .therapist-role{font-size:18px;color:var(--meadow)}

  .referral{text-align:center;padding-top:24px}
  .referral-lead{font-size:19px;line-height:1.35}
  .referral-lead strong{font-weight:700}
  .form{margin:14px 24px 0;background:var(--paper);border-radius:10px;padding:10px 14px;display:grid;grid-template-columns:1fr 1fr;column-gap:24px;row-gap:12px;text-align:left}
  .field{display:flex;align-items:flex-end;gap:8px;font-size:15px}
  .field i{flex:1;border-bottom:1px solid var(--rule);height:12px}
  .spotlight{font-size:24px;font-weight:700;color:var(--coffee);margin-top:18px}
  .fine{text-align:left;font-size:11.5px;line-height:1.35;margin:12px 26px 0}

  .contact-top{display:flex;height:150px;align-items:center;padding:0 26px}
  .contact .brand-dot{width:44px;height:44px}
  .contact .brand-name{font-size:22px}
  .contact .brand{gap:10px;width:210px}
  .divider{width:1px;height:100px;background:var(--rule);margin-right:18px;flex:none}
  .details{font-size:17px;line-height:1.45}
  .details div{display:flex;align-items:center;gap:7px}
  .details svg{width:12px;height:12px;fill:var(--coffee);flex:none}
  .details .addr{margin-top:6px;align-items:flex-start}
  .map{position:absolute;left:0;right:0;bottom:0;height:190px;background:linear-gradient(160deg,var(--map-a) 0%,#e2ded4 55%,#ecd8a8 100%)}
</style>
</head>
<body>

<section class="panel cover">
  <div class="brand"><span class="brand-dot"></span><span class="brand-name">Qovale Day Spa</span></div>
  <p class="slogan">Pure, Calm, Renewing</p>
  <div class="url-band">www.qovalespa.example</div>
  <div class="social" aria-hidden="true"><span></span><span></span><span></span><span></span><span></span></div>
</section>

<section class="panel offer">
  <div class="offer-box">
    <p class="offer-title">WELCOME OFFER</p>
    <p class="offer-line">$119/ Facial, Massage, Mani &amp; Pedi combo*</p>
  </div>
  <p class="feature">Gift Cards Available</p>
  <p class="feature">Walk-Ins Welcome</p>
  <div class="hours">
    <p class="hours-title">HOURS OF PAMPERING:</p>
    <div class="hours-grid">
      <span>Tue-Wed : 10 am – 7 pm</span><span>Sat-Sun : 9 am – 6 pm</span>
      <span>Thu-Fri&nbsp;&nbsp;: 10 am – 8 pm</span><span></span>
    </div>
  </div>
  <div class="therapist">
    <p class="therapist-name">Name Surname</p>
    <p class="therapist-role">Therapist</p>
  </div>
</section>

<section class="panel referral">
  <p class="referral-lead">The best compliment is a referral.<br>Receive <strong>10,000 CALMPerks points</strong> for each you and<br>your friend when you referral a new friend to us**.</p>
  <div class="form">
    <div class="field">You<i></i></div><div class="field">Your friend<i></i></div>
    <div class="field">Phone<i></i></div><div class="field">Phone<i></i></div>
    <div class="field">Email<i></i></div><div class="field">Email<i></i></div>
  </div>
  <p class="spotlight">GET 10,000 POINTS</p>
  <p class="fine">* Welcome package offer valid for first-time Guests only. Includes a Renewal mani&amp; pedi combo, 30 min relaxation massage, and a Renewal facial. Prices subject to change.<br>** CALMPerks points may only be given when a new guest purchase a minimum of $35 from us. Cannot be combined with other specials.</p>
</section>

<section class="panel contact">
  <div class="contact-top">
    <div class="brand"><span class="brand-dot"></span><span class="brand-name">Qovale Day Spa</span></div>
    <span class="divider"></span>
    <div class="details">
      <div><svg viewBox="0 0 12 12"><rect x="3" y="0" width="6" height="12" rx="1.5"/></svg>555-0142-880</div>
      <div><svg viewBox="0 0 12 12"><rect x="0" y="2" width="12" height="8"/></svg>info@qovalespa.example</div>
      <div><svg viewBox="0 0 12 12"><circle cx="6" cy="6" r="6"/></svg>www.qovalespa.example</div>
      <div class="addr"><svg viewBox="0 0 12 12" style="margin-top:4px"><path d="M6 0a4 4 0 0 1 4 4c0 3-4 8-4 8S2 7 2 4a4 4 0 0 1 4-4z"/></svg><span>48 Linden Row, Suite C<br>Fairmont ST 00000</span></div>
    </div>
  </div>
  <div class="map" role="img" aria-label="Street map showing the spa location"></div>
</section>

</body>
</html>
```